Veradine Contracting Folder

Creating a design for the cover of our folders that we pass to our customers

Want to keep the same look as our colors and fonts as attached

```html
<!DOCTYPE html>
<html lang="en">
<head>
<meta charset="utf-8">
<title>Veradine Contracting Folder Cover</title>
<link rel="stylesheet" href="https://fonts.googleapis.com/css2?family=Playfair+Display:wght@700&display=swap">
<style>
  :root {
    --backdrop: #e2e2e2;
    --paper: #f0f0f0;
    --brand-yellow: #dcb22f;
    --brand-yellow-light: #e3c040;
    --brand-blue: #2a33b3;
    --art-grey: #a9a4a0;
    --art-white: #fbfbfb;
  }
  * { margin: 0; padding: 0; box-sizing: border-box; }
  html, body {
    width: 1200px;
    height: 891px;
    overflow: hidden;
    background: var(--backdrop);
  }
  .canvas {
    position: relative;
    width: 1200px;
    height: 891px;
  }
  .folder-cover {
    position: absolute;
    left: 300px;
    top: 21px;
    width: 600px;
    height: 849px;
    background: var(--paper);
    overflow: hidden;
    box-shadow: 0 10px 30px rgba(0,0,0,0.12);
  }
  .colour-band {
    position: absolute;
    left: 0;
    top: 0;
    width: 240px;
    height: 100%;
    background: linear-gradient(160deg, var(--brand-yellow) 0%, var(--brand-yellow-light) 60%, var(--brand-yellow) 100%);
  }
  .company-name {
    position: absolute;
    left: 270px;
    top: 300px;
    font-family: "Playfair Display", serif;
    font-weight: 700;
    font-size: 34px;
    line-height: 40px;
    letter-spacing: 0.08em;
    color: var(--brand-blue);
    white-space: nowrap;
  }
  .painter-artwork {
    position: absolute;
    left: 150px;
    top: 560px;
    width: 340px;
    height: 289px;
    display: block;
  }
</style>
</head>
<body>
  <main class="canvas">
    <section class="folder-cover">
      <div class="colour-band"></div>

      <p class="company-name">Veradine</p>

      <svg class="painter-artwork" viewBox="0 0 340 289" role="img" aria-label="Illustration of a painter on a blue ladder painting white over the yellow band">
        <defs>
          <linearGradient id="artTone" x1="0" y1="0" x2="1" y2="1">
            <stop offset="0" stop-color="#fbfbfb" stop-opacity="0.85"/>
            <stop offset="0.55" stop-color="#a9a4a0" stop-opacity="0.8"/>
            <stop offset="1" stop-color="#2a33b3" stop-opacity="0.7"/>
          </linearGradient>
        </defs>
        <rect x="0" y="0" width="340" height="289" fill="url(#artTone)"/>
      </svg>
    </section>
  </main>
</body>
</html>
```